Christmas social media advert post

I am looking for an eye catching advert for use mainly on social media posts.
The following is the detail of the event.

Christmas special offer-
£10pp,– offer includes –
Half an hour Toboggan track,
Half an hour Slingshot paintballs (20 paintballs pp) and safe target archery (under cover and indoor ranges). Activities all the family from age 4 to grandparents can join in,
Also available – Add on indoor activities including Mini Curling, Zap Blitz, Safe axe throwing, Air juggler – from £3.50pp and age 6plus
Café open for hot food and drinks in the ‘Snug Holly Lodge and the heated Christmas marquee.

A basic idea I put together for what I feel is the important information is -

Christmas Special offer -
Starts Saturday 20th December.
£10pp – offer includes –
Half an hour Slingshot paintballs (20 paintballs pp) and safe target archery (under cover and indoor ranges). Activities all the family from age 4 to grandparents can join in. Booking is essential - details on how below.
Also available Add on indoor activities - including Mini Curling, Zap Blitz, Safe axe throwing, Air juggler – from £3.50pp and age 6plus.
Ages start from 4 plus.
All activities are great for children and adults so perfect for families as well as friends, parties and get togethers.
Free huge car parks,
Booking is easy-
Just Message from messenger (on this post) or email
colin@bluefernleisurepark.co.uk for availability of your preferred date and time.

I would be happy to send the detailed information to enquiries if it meant a better looking advert / post.

Full details are in the picture uploads, feel free to use as much or as little of the information as you feel best.

```html
<!DOCTYPE html>
<html lang="en">
<head>
<meta charset="utf-8">
<title>Christmas Special Offer</title>
<link rel="stylesheet" href="https://fonts.googleapis.com/css2?family=Playfair+Display:wght@600;700&family=Jost:wght@300;400;500;600;700;800&display=swap">
<style>
  :root {
    --red: #c0212f;
    --ink: #1c1c1c;
    --body: #2a2a2a;
    --cream: #f8f1e6;
    --ring: #efe5d3;
    --rule: #cfc3ab;
    --panel: #ffffff;
    --panel-edge: #d9d4cc;
    --holly-red: #c9303a;
    --holly-green: #3f5a3e;
    --tree-green: #235a32;
    --tree-dark: #163d22;
  }
  * { margin: 0; padding: 0; box-sizing: border-box; }
  html, body { width: 1200px; height: 1200px; overflow: hidden; background: var(--cream); }
  .poster {
    position: relative; width: 1200px; height: 1200px; overflow: hidden;
    font-family: "Jost", "Century Gothic", sans-serif; color: var(--body);
    background: var(--cream);
  }
  .floral-border {
    position: absolute; inset: 0;
    background:
      linear-gradient(90deg,
        rgba(201,48,58,0.55) 0, rgba(63,90,62,0.45) 40px, rgba(248,241,230,0) 80px,
        rgba(248,241,230,0) 1120px, rgba(63,90,62,0.45) 1160px, rgba(201,48,58,0.55) 1200px),
      linear-gradient(180deg,
        rgba(201,48,58,0.55) 0, rgba(63,90,62,0.45) 50px, rgba(248,241,230,0) 100px,
        rgba(248,241,230,0) 1100px, rgba(63,90,62,0.45) 1150px, rgba(201,48,58,0.55) 1200px),
      var(--cream);
  }
  .panel {
    position: absolute; left: 95px; top: 113px; width: 1008px; height: 973px;
    background: var(--panel);
    box-shadow: 2px 2px 0 var(--panel-edge);
  }
  .headline {
    position: absolute; left: 0; width: 1200px; text-align: center;
    font-family: "Playfair Display", Georgia, serif; font-weight: 700;
    font-size: 128px; line-height: 1; color: var(--red); top: 118px;
    letter-spacing: -1px;
  }
  .subhead {
    position: absolute; left: 0; width: 1200px; text-align: center;
    font-weight: 300; font-size: 66px; line-height: 1; color: var(--ink); top: 243px;
    letter-spacing: 0.5px;
  }
  .activity-photo {
    position: absolute; width: 148px; height: 148px; border-radius: 50%;
    border: 5px solid var(--ring);
  }
  .photo-cabin   { left: 246px; top: 331px; background: linear-gradient(160deg, #6b4a2c, #d8b48a 60%, #e9d2b0); }
  .photo-curling { left: 526px; top: 309px; background: linear-gradient(170deg, #8a7358, #c9ad88 55%, #e2cfb2); }
  .photo-archery { left: 806px; top: 331px; background: linear-gradient(160deg, #b89d7c, #8c6f52 55%, #5a4636); }
  .photo-axe     { left: 246px; top: 513px; background: linear-gradient(150deg, #2c4da0, #c62a2a 50%, #e6c27a); }
  .photo-gel     { left: 819px; top: 513px; background: linear-gradient(150deg, #6a5350, #3a3d7a 55%, #a25a80); }
  .price-box {
    position: absolute; left: 364px; top: 435px; width: 473px; height: 194px;
    background: var(--panel); border: 2px solid var(--rule); text-align: center;
  }
  .price {
    position: absolute; left: 0; width: 100%; top: 18px;
    font-weight: 700; font-size: 128px; line-height: 1; color: var(--red); letter-spacing: -5px;
  }
  .offer-label {
    position: absolute; left: 0; width: 100%; top: 137px;
    font-weight: 700; font-size: 33px; line-height: 1; color: var(--ink);
  }
  .line {
    position: absolute; left: 0; width: 1200px; text-align: center; white-space: nowrap;
  }
  .lead { font-size: 34px; font-weight: 400; line-height: 1; color: var(--ink); }
  .lead .accent { color: var(--red); font-weight: 500; }
  .copy { font-size: 21.5px; line-height: 26.7px; font-weight: 400; color: var(--body); }
  .copy strong { font-weight: 500; }
  .accent { color: var(--red); }
  .section-title { font-size: 34px; font-weight: 700; color: var(--red); line-height: 1; }
  .rule { position: absolute; left: 413px; width: 376px; height: 1.5px; background: var(--rule); }
  .tree {
    position: absolute; left: 777px; top: 680px; width: 350px; height: 480px;
    background:
      radial-gradient(ellipse 48% 50% at 50% 58%,
        var(--tree-green) 0%, var(--tree-dark) 45%, rgba(22,61,34,0.55) 62%, rgba(255,255,255,0) 78%);
  }
</style>
</head>
<body>
<main class="poster">
  <div class="floral-border" role="img" aria-label="Ornamental border of red flowers, green leaves and red scrollwork"></div>
  <section class="panel"></section>

  <h1 class="headline">Christmias</h1>
  <p class="subhead">SPECIAL OFFER-</p>

  <div class="activity-photo photo-cabin" role="img" aria-label="Photo of the wooden café cabin with hot chocolates and a log burner"></div>
  <div class="activity-photo photo-curling" role="img" aria-label="Photo of a player on the indoor mini curling lane"></div>
  <div class="activity-photo photo-archery" role="img" aria-label="Photo of a player shooting at targets on the archery range"></div>
  <div class="activity-photo photo-axe" role="img" aria-label="Photo of safe throwing axes stuck in a bristle target"></div>
  <div class="activity-photo photo-gel" role="img" aria-label="Photo of a player in the neon-lit gel blaster arena"></div>

  <div class="tree" role="img" aria-label="Illustration of a decorated Christmas tree with red garlands, baubles and a gold star"></div>

  <div class="price-box">
    <div class="price">£10PP,</div>
    <div class="offer-label">OFFER INCLUDES</div>
  </div>

  <p class="line lead" style="top:644px;">Half an hour <span class="accent">Toboggan track,</span></p>
  <div class="rule" style="top:688px;"></div>
  <p class="line lead" style="top:697px;">Half an hour <span class="accent">Slingshot paintballs</span></p>
  <p class="line copy" style="top:731px;">(20 paintballs pp) and safe target archery (under cover<br>and indoor ranges). Activities all the family from<br>age 4 to grandparents can join in,</p>
  <div class="rule" style="top:823px;"></div>
  <p class="line section-title" style="top:830px;">Also available</p>
  <div class="rule" style="top:868px;"></div>
  <p class="line copy" style="top:878px;">Add on indoor activities including Mini Curling,<br>Zap Blitz, Safe axe throwing, Air juggler from<br><strong>£3.50pp</strong> and age 6plus</p>
  <div class="rule" style="top:967px;"></div>
  <p class="line copy" style="top:974px;">Café open for hot food and drinks in the<br>‘<span class="accent">Snug Holly Lodge</span> and the heated<br>Christmas marquee</p>
</main>
</body>
</html>
```